Rack card for a integrative medical practice

Need an eye-catching rack card with our logo with content as provided. We have a membership based holistic medical practice which incorporates western and holistic medicine. We would like to focus on wellness and healthy lifestyle. See uploaded files for what is included in the membership. Would like 2 page rack card color on both sides. Logo must be on the front.

Target Market(s)

People looking for alternative medicine, healthy lifestyle.

Industry/Entity Type

Health and Wellness

Colors
00AB8E
00BBA5
67D7C9
C6EFE9
E9F9F6

Requirements
Must have
• Must spark interest at first sight. Clear message.
Nice to have
• Warm, bright and positive vibe. Organic, neutral and earthy colors.
Should not have
• Traditional medical practice vibe (cold, formal, industrial). No PINK except the logo.

```html
<!DOCTYPE html>
<html lang="en">
<head>
<meta charset="utf-8">
<title>Willowmere Health &amp; Wellness – Rack Card</title>
<link href="https://fonts.googleapis.com/css2?family=Josefin+Sans:wght@400;600;700&display=swap" rel="stylesheet">
<style>
  :root {
    --teal-deep: #00AB8E;
    --teal: #00BBA5;
    --teal-soft: #67D7C9;
    --teal-pale: #C6EFE9;
    --mint: #E9F9F6;
    --pink: #E5408A;
    --ink: #2b2b2b;
    --grey-text: #555;
    --stage: #F4F4F4;
    --paper: #FFFFFF;
    --rule: #E2E2E2;
  }
  * { box-sizing: border-box; margin: 0; padding: 0; }
  html, body { width: 1200px; height: 1200px; overflow: hidden; }
  body {
    background: var(--stage);
    font-family: "Josefin Sans", sans-serif;
    color: var(--ink);
    position: relative;
  }
  .card {
    position: absolute;
    top: 98px;
    width: 460px;
    height: 1004px;
    overflow: hidden;
    text-align: center;
  }
  .card--front { left: 128px; background: var(--mint); }
  .card--back  { left: 612px; background: var(--paper); }

  .abs { position: absolute; left: 0; width: 100%; }

  /* Front */
  .front-photo {
    position: absolute; left: 0; top: 0; width: 460px; height: 530px;
    background: linear-gradient(160deg, #e9dcdc 0%, #f3eeee 35%, #d8c9c4 60%, #b78c8e 100%);
  }
  .front-wave { position: absolute; left: 0; top: 0; }
  .brand-name {
    font-weight: 600;
    color: var(--pink);
    line-height: 1;
  }
  .brand-name__main { display: block; font-size: 40px; letter-spacing: 6px; }
  .brand-name__sub { display: block; font-size: 15px; letter-spacing: 6px; margin-top: 14px; }
  .front-brand { top: 578px; }
  .tagline {
    position: absolute; left: 50px; width: 361px; top: 689px;
    border-top: 1.5px solid var(--teal-soft);
    border-bottom: 1.5px solid var(--teal-soft);
    padding: 10px 0 10px;
    font-size: 16px; line-height: 26px; text-transform: uppercase; letter-spacing: .5px;
  }
  .contact__phone { font-size: 36px; font-weight: 600; color: var(--teal-deep); line-height: 1.1; }
  .contact__addr { font-size: 22px; font-weight: 600; line-height: 33px; margin-top: 6px; }
  .contact__web { font-size: 20px; letter-spacing: 1.5px; color: var(--grey-text); margin-top: 12px; }
  .contact { top: 828px; }
  .corner-leaf {
    position: absolute; left: 0; bottom: 0; width: 120px; height: 80px;
    background: radial-gradient(ellipse at 30% 100%, var(--teal-pale) 0%, rgba(198,239,233,.4) 60%, transparent 75%);
  }

  /* Back */
  .back-header { position: absolute; left: 0; top: 0; }
  .back-brand { top: 118px; }
  .back-brand .brand-name { color: var(--paper); }
  .back-brand .brand-name__main { font-size: 32px; letter-spacing: 5px; }
  .back-brand .brand-name__sub { font-size: 10px; margin-top: 10px; }
  .membership-title {
    top: 296px; color: var(--pink); font-weight: 700; font-size: 24px; line-height: 31px;
    text-transform: uppercase;
  }
  .benefits { position: absolute; left: 32px; width: 396px; top: 370px; list-style: none; }
  .benefits li {
    font-size: 17.5px; line-height: 30px; padding: 3px 0 2px;
    border-bottom: 1.5px solid var(--rule);
    letter-spacing: .3px;
  }
  .benefits li:nth-child(even) { color: var(--teal-deep); }
  .benefits li:last-child { border-bottom: none; }
  .join {
    position: absolute; left: 119px; top: 760px; width: 223px; height: 50px;
    border: 1.5px solid var(--pink); color: var(--pink);
    font-weight: 700; font-size: 24px; line-height: 52px;
  }
</style>
</head>
<body>

<section class="card card--front">
  <div class="front-photo" role="img" aria-label="Photo of a woman in a white linen shirt meditating with a hand on her heart, flowers beside her"></div>
  <svg class="front-wave" width="460" height="560" viewBox="0 0 460 560" aria-hidden="true">
    <path d="M0,300 C30,380 60,420 130,440 C180,455 205,470 230,508 C255,470 280,455 330,440 C400,420 430,380 460,288 V560 H0 Z" fill="#CFCFCF"/>
    <path d="M0,470 C70,505 160,470 205,500 C218,508 224,514 230,520 C236,514 242,508 255,500 C300,470 390,505 460,470 V560 H0 Z" fill="#E6E6E6"/>
    <path d="M0,484 C70,516 160,482 205,508 C218,516 224,520 230,524 C236,520 242,516 255,508 C300,482 390,516 460,484 V560 H0 Z" fill="var(--paper)"/>
    <path d="M0,490 C70,522 160,488 205,514 C218,521 224,525 230,530 C236,525 242,521 255,514 C300,488 390,522 460,490 V560 H0 Z" fill="var(--mint)"/>
  </svg>

  <div class="abs front-brand">
    <p class="brand-name">
      <span class="brand-name__main">WILLOWMERE</span>
      <span class="brand-name__sub">HEALTH &amp; WELLNESS</span>
    </p>
  </div>

  <p class="tagline">A direct primary care practice<br>focused on a more holistic<br>and personal approach to medicine.</p>

  <div class="abs contact">
    <p class="contact__phone">555-014-2290</p>
    <p class="contact__addr">1214 Orchard Ave., STE 2B<br>Brookhaven</p>
    <p class="contact__web">willowmerehealth.com</p>
  </div>

  <div class="corner-leaf" role="img" aria-label="Soft teal leaf line drawing in the corner"></div>
</section>

<section class="card card--back">
  <svg class="back-header" width="460" height="290" viewBox="0 0 460 290" aria-hidden="true">
    <path d="M0,0 H460 V250 C400,230 360,248 310,256 C270,262 250,272 230,288 C210,272 190,262 150,256 C100,248 60,230 0,250 Z" fill="#E4E4E4"/>
    <path d="M0,0 H460 V232 C400,214 360,238 310,244 C270,250 250,258 230,274 C210,258 190,250 150,244 C100,238 60,214 0,232 Z" fill="var(--pink)"/>
    <path d="M0,0 H460 V40 C430,40 415,90 395,135 C370,195 330,215 290,228 C260,238 245,250 230,268 C215,250 200,238 170,228 C130,215 90,195 65,135 C45,90 30,40 0,40 Z" fill="#E8E8E8"/>
    <path d="M0,0 H460 V32 C430,32 412,84 392,130 C368,188 328,207 290,220 C260,230 245,242 230,258 C215,242 200,230 170,220 C132,207 92,188 68,130 C48,84 30,32 0,32 Z" fill="var(--teal)"/>
  </svg>

  <div class="abs back-brand">
    <p class="brand-name">
      <span class="brand-name__main">WILLOWMERE</span>
      <span class="brand-name__sub">HEALTH &amp; WELLNESS</span>
    </p>
  </div>

  <h2 class="abs membership-title">What's included<br>in your membership :</h2>

  <ul class="benefits">
    <li>Unlimited office visits with no copay</li>
    <li>Direct communication with your doctor</li>
    <li>Discounted labs, imaging and medications</li>
    <li>Free initial acupuncture session ($250 value).</li>
    <li>2 Vitascan testings per year ($100 value)</li>
    <li>Discounts for supplements and health<br>products in the clinic</li>
    <li>Discounts for iv vitamin infusion therapy</li>
    <li>Personalized nutrition plan after advanced<br>testing such as gut microbiome, hormonal,<br>metabolism test, etc.</li>
  </ul>

  <p class="join">JOIN US TODAY!</p>

  <div class="abs contact">
    <p class="contact__phone">555-014-2290</p>
    <p class="contact__addr">1214 Orchard Ave., STE 2B<br>Brookhaven</p>
    <p class="contact__web">willowmerehealth.com</p>
  </div>

  <div class="corner-leaf" role="img" aria-label="Soft teal leaf line drawing in the corner"></div>
</section>

</body>
</html>
```